Business Card Design for a Design/Build Firm

Kestrel Forge Partners, Inc. is a firm providing construction professional project management and architectural design services to an international clientele. Contemporary. "Green" movement aware. Business card to have back design/logo. Cards will be on high gloss paper

Target Market(s)

Building Developers and Owners

Industry/Entity Type

Construction

Requirements
Nice to have
• We really would like to use the acronym "KFP" as main focal point fo card design. Company will be known as KFP.
Should not have
• No globes or abstract images of buildings.

```html
<!DOCTYPE html>
<html lang="en">
<head>
<meta charset="utf-8">
<title>Kestrel Forge Partners, Inc. — Business Card</title>
<link rel="stylesheet" href="https://fonts.googleapis.com/css2?family=EB+Garamond:wght@400;500&display=swap">
<style>
  :root {
    --backdrop: #2a2a2a;
    --card-dark: #1b1b1b;
    --brand-red: #8a0505;
    --rule-grey: #555555;
    --divider-black: #050505;
    --text-light: #f2f2f2;
    --logo-white: #ffffff;
  }
  * { box-sizing: border-box; margin: 0; padding: 0; }
  html, body {
    width: 1200px; height: 900px; overflow: hidden;
    background: var(--backdrop);
  }
  .canvas { position: relative; width: 1200px; height: 900px; }

  .card {
    position: absolute; width: 640px; height: 380px;
    background: var(--card-dark);
    font-family: "EB Garamond", Georgia, serif;
    color: var(--text-light);
    overflow: hidden;
    box-shadow: 0 10px 24px rgba(0,0,0,.55);
  }
  .card--front { left: 80px; top: 50px; }
  .card--back { left: 480px; top: 470px; }

  .band { position: absolute; left: 0; width: 100%; height: 76px; background: var(--brand-red); }
  .band--top { top: 0; }
  .band--bottom { bottom: 0; }
  .rule { position: absolute; left: 0; width: 100%; height: 6px; background: var(--rule-grey); }
  .rule--top { top: 82px; }
  .rule--bottom { bottom: 82px; }

  .wordmark {
    position: absolute; display: flex; align-items: center; gap: 12px;
  }
  .wordmark__square { width: 30px; height: 30px; background: var(--logo-white); }
  .wordmark__name {
    font-size: 76px; font-weight: 400; line-height: 1;
    letter-spacing: 6px; color: var(--logo-white);
  }
  .card--front .wordmark { left: 96px; top: 148px; }
  .card--back .wordmark { left: 52px; top: 150px; }

  .divider { position: absolute; width: 5px; background: var(--divider-black); }
  .card--front .divider { left: 340px; top: 130px; height: 120px; }
  .card--back .divider { left: 312px; top: 106px; height: 168px; }

  .company-name {
    position: absolute; left: 362px; top: 138px;
    font-size: 22px; line-height: 22px; text-transform: uppercase; letter-spacing: .5px;
  }

  .contact { position: absolute; left: 336px; top: 106px; }
  .contact__name { color: var(--brand-red); font-size: 22px; line-height: 24px; }
  .contact__title { font-size: 16px; line-height: 18px; margin-bottom: 22px; }
  .contact__list { list-style: none; font-size: 14px; line-height: 20px; }
  .contact__list li { display: flex; }
  .contact__label { color: var(--brand-red); width: 24px; flex: none; }
  .contact__list .contact__small { font-size: 11px; }
</style>
</head>
<body>
<main class="canvas">

  <section class="card card--front" aria-label="Card front">
    <div class="band band--top"></div>
    <div class="rule rule--top"></div>
    <div class="wordmark">
      <span class="wordmark__square"></span>
      <span class="wordmark__name">KFP</span>
    </div>
    <div class="divider"></div>
    <p class="company-name">Kestrel<br>Forge<br>Partners, Inc.</p>
    <div class="rule rule--bottom"></div>
    <div class="band band--bottom"></div>
  </section>

  <section class="card card--back" aria-label="Card back">
    <div class="band band--top"></div>
    <div class="rule rule--top"></div>
    <div class="wordmark">
      <span class="wordmark__square"></span>
      <span class="wordmark__name">KFP</span>
    </div>
    <div class="divider"></div>
    <div class="contact">
      <p class="contact__name">Marcus Hale</p>
      <p class="contact__title">Director</p>
      <ul class="contact__list">
        <li><span class="contact__label">A :</span><span>2280 Larkspur Court, Suite 210<br>Oakview, CA 94520</span></li>
        <li class="contact__small"><span class="contact__label">P :</span><span>921 555 0188</span></li>
        <li><span class="contact__label">E :</span><span>mhale@kfpartners.com</span></li>
        <li><span class="contact__label">W :</span><span>www.kfpartners.com</span></li>
      </ul>
    </div>
    <div class="rule rule--bottom"></div>
    <div class="band band--bottom"></div>
  </section>

</main>
</body>
</html>
```